Birchfield Dental Care Stationery

create stationery, business cards and envelops for business. Use current logo on website but open to new fonts for the business name. Business name is Birchfield Dental Care, would like below the name added "Cosmetic - Family - Implants" Website is www.birchfielddentalcareQX.example. I would like to have modern look, clean, and professional. The water mark of the logo is a great thing to ad as well.

Target Market(s)

General public, Families, Cosmetic, Implant

Industry/Entity Type

Dental

Font styles to use
Sans Serif

Colors
9bcb3c
000000
757575
c9c9c9

Requirements
Must have
• Would like to see different versions of the current logo. Improvements, color, sytle, and class.
Nice to have
• current font has double "oo" in the Birchfield logo, does not need to have with new logo.

```html
<!DOCTYPE html>
<html lang="en">
<head>
<meta charset="utf-8">
<title>Birchfield Dental Care Stationery</title>
<link href="https://fonts.googleapis.com/css2?family=Open+Sans:wght@400;600&display=swap" rel="stylesheet">
<style>
  :root {
    --green: #8cb84a;
    --slate: #3d444e;
    --paper: #f4f4f3;
    --backdrop: #e6e6e6;
    --ink-light: #ffffff;
    --ink-muted: #757575;
  }
  * { margin: 0; padding: 0; box-sizing: border-box; }
  html, body { width: 1200px; height: 795px; overflow: hidden; }
  body {
    background: var(--backdrop);
    font-family: "Open Sans", sans-serif;
    position: relative;
  }
  .piece { position: absolute; overflow: hidden; }
  .swoosh { position: absolute; left: 0; bottom: 0; width: 100%; display: block; }

  /* brand lockup */
  .lockup { position: absolute; display: flex; align-items: center; gap: 4px; }
  .lockup-circle { border-radius: 50%; border: 1.5px solid var(--green); flex: none; }
  .lockup-text { display: flex; flex-direction: column; line-height: 1; }
  .lockup-name { font-weight: 600; color: var(--slate); letter-spacing: .04em; text-transform: uppercase; white-space: nowrap; }
  .lockup-name span { display: block; }
  .lockup-tag { color: var(--ink-muted); letter-spacing: .08em; text-transform: uppercase; white-space: nowrap; margin-top: 2px; }
  .lockup.on-dark .lockup-name, .lockup.on-dark .lockup-tag { color: var(--ink-light); }
  .lockup.on-green .lockup-circle { border-color: var(--ink-light); }
  .lockup.on-green .lockup-name, .lockup.on-green .lockup-tag { color: var(--ink-light); }

  /* letterhead */
  .letterhead { left: 292px; top: 99px; width: 293px; height: 415px; background: var(--paper); }
  .letterhead .lockup { left: 97px; top: 31px; }
  .letterhead .lockup-circle { width: 30px; height: 30px; }
  .letterhead .lockup-name { font-size: 10px; }
  .letterhead .lockup-tag { font-size: 3.6px; }
  .letterhead-footer { position: absolute; left: 0; bottom: 6px; width: 100%; text-align: center; color: var(--ink-light); font-size: 4.6px; line-height: 1.8; }

  /* presentation folder */
  .folder { left: 634px; top: 80px; width: 348px; height: 437px; background: var(--slate); }
  .folder-spine { position: absolute; left: 3px; top: 0; width: 18px; height: 100%; background: var(--green); }
  .folder .lockup { left: 96px; top: 193px; gap: 6px; }
  .folder .lockup-circle { width: 50px; height: 50px; }
  .folder .lockup-name { font-size: 17px; }
  .folder .lockup-tag { font-size: 6.2px; margin-top: 3px; }

  /* business cards */
  .card-front { left: 186px; top: 550px; width: 133px; height: 76px; background: var(--paper); }
  .card-person { position: absolute; top: 4px; width: 100%; text-align: center; }
  .card-person-name { font-size: 4.4px; color: var(--green); font-weight: 600; }
  .card-person-role { font-size: 2.8px; color: var(--slate); }
  .card-front .lockup { left: 36px; top: 22px; }
  .card-front .lockup-circle { width: 16px; height: 16px; }
  .card-front .lockup-name { font-size: 5.6px; }
  .card-front .lockup-tag { font-size: 2.2px; margin-top: 1px; }
  .card-contact { position: absolute; left: 0; bottom: 3px; width: 100%; text-align: center; color: var(--ink-light); font-size: 2.9px; line-height: 1.7; }

  .card-back { left: 186px; top: 647px; width: 133px; height: 75px; background: var(--green); }
  .card-back .lockup { left: 30px; top: 26px; }
  .card-back .lockup-circle { width: 20px; height: 20px; }
  .card-back .lockup-name { font-size: 6.6px; }
  .card-back .lockup-tag { font-size: 2.6px; margin-top: 1px; }

  /* envelope front */
  .envelope-front { left: 353px; top: 561px; width: 329px; height: 157px; background: var(--paper); }
  .envelope-front .lockup { left: 15px; top: 16px; }
  .envelope-front .lockup-circle { width: 21px; height: 21px; }
  .envelope-front .lockup-name { font-size: 7.6px; }
  .envelope-front .lockup-tag { font-size: 2.8px; margin-top: 1px; }
  .envelope-return { position: absolute; left: 19px; bottom: 8px; color: var(--ink-light); font-size: 4.4px; line-height: 1.6; }

  /* envelope back */
  .envelope-back { left: 713px; top: 561px; width: 329px; height: 157px; background: var(--paper); }
  .envelope-flap { position: absolute; left: 0; top: 0; width: 100%; height: 56px; display: block; }
  .flap-mark { position: absolute; left: 153px; top: 12px; width: 22px; height: 22px; border-radius: 50%; border: 1.5px solid var(--ink-light); }
  .flap-url { position: absolute; top: 40px; width: 100%; text-align: center; color: var(--ink-light); font-size: 3.6px; letter-spacing: .05em; }
</style>
</head>
<body>

  <section class="piece letterhead" aria-label="Letterhead">
    <div class="lockup">
      <span class="lockup-circle"></span>
      <span class="lockup-text">
        <span class="lockup-name"><span>Birchfield</span><span>Dental Care</span></span>
        <span class="lockup-tag">Cosmetic - Family - Implants</span>
      </span>
    </div>
    <svg class="swoosh" viewBox="0 0 293 56" height="56" preserveAspectRatio="none" aria-hidden="true">
      <path d="M0 0 Q146 54 293 0 L293 56 L0 56 Z" fill="var(--slate)"/>
      <path d="M0 0 Q146 48 293 0 Q146 60 0 0 Z" fill="var(--green)"/>
    </svg>
    <div class="letterhead-footer">
      <div>412 N Birchfield Ave, Alder Falls, QX 00000-1111</div>
      <div>&#9742; 555-014-2290 &nbsp;&#9993; helen@birchfielddentalcareQX.example &nbsp;&#9679; www.birchfielddentalcareQX.example</div>
    </div>
  </section>

  <section class="piece folder" aria-label="Presentation folder">
    <div class="folder-spine"></div>
    <div class="lockup on-dark">
      <span class="lockup-circle"></span>
      <span class="lockup-text">
        <span class="lockup-name"><span>Birchfield</span><span>Dental Care</span></span>
        <span class="lockup-tag">Cosmetic - Family - Implants</span>
      </span>
    </div>
  </section>

  <section class="piece card-front" aria-label="Business card front">
    <div class="card-person">
      <div class="card-person-name">Dr. Helen Marsh D.D.S.</div>
      <div class="card-person-role">Alder Falls Cosmetic, Family, &amp; Sedation Dentist</div>
    </div>
    <div class="lockup">
      <span class="lockup-circle"></span>
      <span class="lockup-text">
        <span class="lockup-name"><span>Birchfield</span><span>Dental Care</span></span>
        <span class="lockup-tag">Cosmetic - Family - Implants</span>
      </span>
    </div>
    <svg class="swoosh" viewBox="0 0 133 36" height="36" preserveAspectRatio="none" aria-hidden="true">
      <path d="M0 4 Q66 22 133 4 L133 36 L0 36 Z" fill="var(--slate)"/>
      <path d="M0 4 Q66 19 133 4 Q66 25 0 4 Z" fill="var(--green)"/>
    </svg>
    <div class="card-contact">
      <div>412 N Birchfield Ave, Alder Falls, QX 00000-1111</div>
      <div>&#9742; 555-014-2290 &nbsp;&#9993; helen@birchfielddentalcareQX.example</div>
      <div>www.birchfielddentalcareQX.example</div>
    </div>
  </section>

  <section class="piece card-back" aria-label="Business card back">
    <div class="lockup on-green">
      <span class="lockup-circle"></span>
      <span class="lockup-text">
        <span class="lockup-name"><span>Birchfield</span><span>Dental Care</span></span>
        <span class="lockup-tag">Cosmetic - Family - Implants</span>
      </span>
    </div>
  </section>

  <section class="piece envelope-front" aria-label="Envelope front">
    <div class="lockup">
      <span class="lockup-circle"></span>
      <span class="lockup-text">
        <span class="lockup-name"><span>Birchfield</span><span>Dental Care</span></span>
        <span class="lockup-tag">Cosmetic - Family - Implants</span>
      </span>
    </div>
    <svg class="swoosh" viewBox="0 0 329 60" height="60" preserveAspectRatio="none" aria-hidden="true">
      <path d="M0 4 Q164 66 329 0 L329 60 L0 60 Z" fill="var(--slate)"/>
      <path d="M0 4 Q164 58 329 0 Q164 72 0 4 Z" fill="var(--green)"/>
    </svg>
    <div class="envelope-return">
      <div>412 N Birchfield Ave</div>
      <div>Alder Falls, QX 00000-1111</div>
    </div>
  </section>

  <section class="piece envelope-back" aria-label="Envelope back">
    <svg class="envelope-flap" viewBox="0 0 329 56" preserveAspectRatio="none" aria-hidden="true">
      <path d="M0 0 L329 0 L325 48 Q324 56 316 56 L13 56 Q5 56 4 48 Z" fill="var(--green)"/>
    </svg>
    <span class="flap-mark"></span>
    <div class="flap-url">www.birchfielddentalcareQX.example</div>
  </section>

</body>
</html>
```